Pierlyn- Vorta Ridgeline Car Wrap Using Branding and Logo

We need to take our logo and branding and wrap a 2016 Vorta Ridgeline. See pierlyn.app for more info. This vehicle will be used by the sales and marketing teams to visit boat shows, docks, and boat ramps. Ple

Target Market(s)

Target Market is Boaters and Dock/Boat Slip Owners

Industry/Entity Type

Boating, Docks, Marina

Font styles to use
Serif
Other font styles liked:
• Our font

Colors
0054AA
0677BA
7BADD7
CADEEF
E8F1F8
FFC000
F8CF3A
FAE287
FDF2CF
FEFAEE

Requirements
Must have
• Logo, email, phone, pierlyn.app, company brand, picture of a dock with a boat on it
Nice to have
• Like to see some creative, eye catching but clear designs

```html
<!DOCTYPE html>
<html lang="en">
<head>
<meta charset="utf-8">
<title>Pierlyn – Vehicle Wrap Panel</title>
<link rel="stylesheet" href="https://fonts.googleapis.com/css2?family=Alegreya+SC:wght@700;800&family=Alegreya+Sans:wght@700&display=swap">
<style>
  :root {
    --teal: #256574;
    --teal-deep: #1f4550;
    --ink: #1d3f4a;
    --orange: #f8a31a;
    --white: #ffffff;
    --icon-bg: #e9eff1;
  }
  * { margin: 0; padding: 0; box-sizing: border-box; }
  html, body { width: 1200px; height: 429px; overflow: hidden; background: var(--white); }
  .wrap-panel { position: relative; width: 1200px; height: 429px; overflow: hidden; }
  .backdrop { position: absolute; inset: 0; }
  .brand { position: absolute; left: 329px; top: 254px; display: flex; align-items: center; gap: 16px; }
  .brand-mark { width: 48px; height: 48px; border-radius: 50%; background: var(--ink); }
  .brand-name {
    font-family: "Alegreya SC", Georgia, serif; font-weight: 800;
    font-size: 36px; letter-spacing: 1.5px; color: var(--ink); line-height: 1;
  }
  .tagline {
    position: absolute; left: 335px; top: 314px;
    font-family: "Alegreya Sans", Arial, sans-serif; font-weight: 700;
    font-size: 18px; letter-spacing: 0.6px; color: var(--ink); white-space: nowrap;
  }
  .contacts { position: absolute; left: 663px; top: 228px; list-style: none; }
  .contact { display: flex; align-items: center; height: 31px; margin-bottom: 21px; }
  .contact-icon {
    width: 31px; height: 31px; border-radius: 50%;
    border: 1.5px solid var(--ink); background: var(--icon-bg);
    display: flex; align-items: center; justify-content: center; flex: none;
  }
  .contact-text {
    margin-left: 14px;
    font-family: "Alegreya Sans", Arial, sans-serif; font-weight: 700;
    font-size: 19px; letter-spacing: 0.4px; color: var(--ink); white-space: nowrap;
  }
  .panel-code {
    position: absolute; right: 6px; top: 399px;
    font-family: Arial, Helvetica, sans-serif; font-size: 8px; color: #333;
  }
</style>
</head>
<body>
<main class="wrap-panel">
  <svg class="backdrop" width="1200" height="429" viewBox="0 0 1200 429" aria-hidden="true">
    <rect width="1200" height="381" fill="var(--teal)"/>
    <path d="M0,130 C70,250 170,335 280,381 L0,381 Z" fill="var(--teal-deep)"/>
    <path d="M1200,140 C1130,250 1050,330 936,381 L1200,381 Z" fill="var(--teal-deep)"/>
    <path d="M164,0 C164,150 250,285 368,381 L834,381 C950,290 1035,150 1035,0 Z" fill="var(--white)"/>
    <rect y="381" width="1200" height="14" fill="var(--orange)"/>
    <rect y="395" width="1200" height="19" fill="var(--white)"/>
    <rect y="414" width="1200" height="15" fill="var(--orange)"/>
  </svg>

  <div class="brand">
    <span class="brand-mark"></span>
    <span class="brand-name">Pierlyn</span>
  </div>
  <p class="tagline">BOOK YOUR NEXT ADVENTURE</p>

  <ul class="contacts">
    <li class="contact">
      <span class="contact-icon">
        <svg width="14" height="14" viewBox="0 0 24 24"><path fill="var(--ink)" d="M6.6 10.8a15.1 15.1 0 0 0 6.6 6.6l2.2-2.2c.3-.3.7-.4 1-.2 1.1.4 2.3.6 3.6.6.6 0 1 .4 1 1V20c0 .6-.4 1-1 1A17 17 0 0 1 3 4c0-.6.4-1 1-1h3.5c.6 0 1 .4 1 1 0 1.3.2 2.5.6 3.6.1.3 0 .7-.2 1z"/></svg>
      </span>
      <span class="contact-text">+1555-014-2270</span>
    </li>
    <li class="contact">
      <span class="contact-icon">
        <svg width="16" height="12" viewBox="0 0 16 12"><rect x="0.8" y="0.8" width="14.4" height="10.4" fill="none" stroke="var(--ink)" stroke-width="1.6"/><path d="M1 1l7 6 7-6M1 11l5-5M15 11l-5-5" fill="none" stroke="var(--ink)" stroke-width="1.4"/></svg>
      </span>
      <span class="contact-text">info@pierlyn.app</span>
    </li>
    <li class="contact">
      <span class="contact-icon">
        <svg width="15" height="15" viewBox="0 0 24 24" fill="none" stroke="var(--ink)" stroke-width="2.2"><circle cx="12" cy="12" r="10"/><path d="M2 12h20M12 2c3 3 3 17 0 20M12 2c-3 3-3 17 0 20M4 7h16M4 17h16"/></svg>
      </span>
      <span class="contact-text">pierlyn.app</span>
    </li>
  </ul>

  <span class="panel-code">C50</span>
</main>
</body>
</html>
```